DJ Kovan Threl

I'm looking for a professional but still artsy/progressive design. I come from a hip hop/club DJ background playing a lot of underground music but have switched to doing more corporate parties and weddings recently. I am all about keeping the dancefloor moving and emotionally connecting with the crowd. I'd like a trendy/updated color palette. Something that's clean enough that looks professional but also trendy enough to convey that by the end of the night we'll be sweatily dancing to the latest hits. Some designers/artists I like: Rolo Partague, Wendel Ashby, Tobiah Crane, Vexmor 3100, Lyle Brandish.

```html
<!DOCTYPE html>
<html lang="en">
<head>
<meta charset="utf-8">
<title>DJ Kovan Threl – Business Card</title>
<link rel="stylesheet" href="https://fonts.googleapis.com/css2?family=Bebas+Neue&family=Open+Sans:wght@400&display=swap">
<style>
  :root {
    --backdrop: #5b5b5b;
    --card-light: #f3f3f3;
    --brand-orange: #e8781b;
    --ink: #141414;
    --ink-soft: #222222;
    --white: #ffffff;
  }
  * { box-sizing: border-box; margin: 0; padding: 0; }
  html, body {
    width: 1200px;
    height: 900px;
    overflow: hidden;
    background: var(--backdrop);
  }
  .canvas {
    position: relative;
    width: 1200px;
    height: 900px;
  }
  .card {
    position: absolute;
    top: 200px;
    width: 310px;
    height: 502px;
  }
  .card--front {
    left: 253px;
    background: var(--card-light);
    border-radius: 66px 0 66px 0;
  }
  .card--back {
    left: 627px;
    background: var(--brand-orange);
    border-radius: 0 66px 0 66px;
  }
  .wordmark {
    position: absolute;
    left: 0;
    right: 0;
    text-align: center;
    font-family: "Bebas Neue", sans-serif;
    font-weight: 400;
    font-size: 46px;
    line-height: 1;
    letter-spacing: 0.5px;
  }
  .card--front .wordmark { top: 142px; color: var(--ink); }
  .card--back .wordmark { top: 234px; color: var(--white); }

  .contact {
    position: absolute;
    left: 32px;
    top: 298px;
    font-family: "Open Sans", sans-serif;
    color: var(--ink-soft);
  }
  .contact__name {
    font-family: "Bebas Neue", sans-serif;
    font-size: 27px;
    line-height: 1;
    color: var(--brand-orange);
    letter-spacing: 0.3px;
  }
  .contact__role {
    font-size: 15px;
    line-height: 20px;
    margin-top: 1px;
  }
  .contact__list {
    list-style: none;
    margin-top: 6px;
  }
  .contact__item {
    display: flex;
    align-items: center;
    font-size: 15px;
    line-height: 18px;
  }
  .contact__icon {
    width: 12px;
    height: 12px;
    margin-right: 4px;
    fill: var(--brand-orange);
    flex: none;
  }
  .contact__address {
    font-size: 15px;
    line-height: 18px;
    margin-top: 8px;
    font-style: normal;
  }
  .back__url {
    position: absolute;
    left: 0;
    right: 0;
    top: 437px;
    text-align: center;
    font-family: "Open Sans", sans-serif;
    font-size: 14px;
    color: var(--white);
  }
</style>
</head>
<body>
<main class="canvas">
  <section class="card card--front">
    <div class="wordmark">DJ Kovan Threl</div>
    <div class="contact">
      <div class="contact__name">Marlon Vesty</div>
      <div class="contact__role">Managing Director</div>
      <ul class="contact__list">
        <li class="contact__item">
          <svg class="contact__icon" viewBox="0 0 12 12" aria-hidden="true"><path d="M1 4c0-1.5 2-2.5 5-2.5S11 2.5 11 4v1H8.5V3.8h-5V5H1z M3 6h6l1.5 4.5h-9z"/></svg>
          044-123 456 789
        </li>
        <li class="contact__item">
          <svg class="contact__icon" viewBox="0 0 12 12" aria-hidden="true"><path d="M3.5 0.5h5a1 1 0 0 1 1 1v9a1 1 0 0 1-1 1h-5a1 1 0 0 1-1-1v-9a1 1 0 0 1 1-1zM4 2v7h4V2zM5.5 9.6h1v1h-1z"/></svg>
          044-123 456 789
        </li>
        <li class="contact__item">
          <svg class="contact__icon" viewBox="0 0 12 12" aria-hidden="true"><path d="M1 3h10v6.5H1zM1.6 3.4L6 7l4.4-3.6v0.9L6 7.9 1.6 4.3z" fill-rule="evenodd"/></svg>
          info@webname.com
        </li>
        <li class="contact__item">
          <svg class="contact__icon" viewBox="0 0 12 12" aria-hidden="true"><circle cx="6" cy="6" r="5.2"/></svg>
          www.websitename.com
        </li>
      </ul>
      <address class="contact__address">12345, Address Goes Here<br>Country Name, 123456.</address>
    </div>
  </section>

  <section class="card card--back">
    <div class="wordmark">DJ Kovan Threl</div>
    <div class="back__url">www.websitename.com</div>
  </section>
</main>
</body>
</html>
```